Design a logo and Business Cards for Corbel Ridge Banquet and Convention Centre

Hi there
I need a logo and business card done . It is for Corbel Ridge Manor Banquet & Convention Centre. Please look at the picture in the attached file, the logo needs to have a very classy look and a WOW factor, using the contrast between the Dark Grey, the light green and Gold. It has to be an elegant card. if you can do a logo for Corbel Ridge Manor Banquet & Convention Centre. That would help to. the contest is for 20.00 and we need this done asap!
https://www.kinlinkpages.com/pages/Corbel-Ridge-Manor-Banquet-Hall/917362048153609?bookmark_t=page
Delia Ponzanelli
Director of Catering & Events
289-555-0163
delia@corbelridgemanor.com
the image is a reference for a color guide. The card should have rounded corners. Artwork needs to be in .ai min 300 dpi
the image It is green , gold and charcoal grey. So please use these.
Thanks
Gus

```html
<!DOCTYPE html>
<html lang="en">
<head>
<meta charset="utf-8">
<title>Corbel Ridge Manor – Business Cards</title>
<link rel="stylesheet" href="https://fonts.googleapis.com/css2?family=Montserrat:wght@500&family=Open+Sans:wght@400;600&display=swap">
<style>
  :root {
    --backdrop: #e6e8e2;
    --card-white: #ffffff;
    --charcoal: #2b2a29;
    --gold: #d8a324;
    --gold-soft: #e2b53c;
    --sage: #9cb86a;
    --caption: #3a3a3a;
    --contact: #e8e6e1;
    --card-radius: 14px;
  }
  html, body {
    margin: 0;
    padding: 0;
    overflow: hidden;
  }
  .canvas {
    position: relative;
    width: 1155px;
    height: 1200px;
    background: var(--backdrop);
    overflow: hidden;
  }
  .card {
    position: absolute;
    left: 199px;
    width: 712px;
    height: 410px;
    border-radius: var(--card-radius);
    overflow: hidden;
    box-shadow: 0 4px 14px rgba(0,0,0,0.18);
  }
  .card-front {
    top: 122px;
    background: var(--card-white);
    border: 1px solid #cfcfcf;
    box-sizing: border-box;
  }
  .card-back {
    top: 651px;
    background: var(--charcoal);
  }
  .brand {
    position: absolute;
    text-align: center;
    font-family: "Open Sans", sans-serif;
    font-weight: 600;
    color: var(--gold);
    line-height: 1.3;
  }
  .brand-mark {
    display: block;
    width: 18px;
    height: 18px;
    margin: 0 auto 14px;
    border-radius: 50%;
    background: var(--sage);
  }
  .card-front .brand {
    left: 20px;
    width: 354px;
    top: 168px;
    font-size: 18px;
  }
  .card-back .brand {
    left: 0;
    width: 712px;
    top: 160px;
    font-size: 26px;
  }
  .contact-panel {
    position: absolute;
    left: 385px;
    top: 24px;
    width: 304px;
    height: 366px;
    background: var(--charcoal);
    border-radius: 8px;
    font-family: "Open Sans", sans-serif;
  }
  .person-name {
    position: absolute;
    left: 46px;
    top: 38px;
    margin: 0;
    font-size: 17px;
    font-weight: 400;
    color: var(--gold-soft);
  }
  .person-role {
    position: absolute;
    left: 46px;
    top: 62px;
    margin: 0;
    font-size: 14px;
    color: var(--gold-soft);
  }
  .contact-list {
    position: absolute;
    left: 44px;
    top: 194px;
    margin: 0;
    padding: 0;
    list-style: none;
    font-size: 14px;
    color: var(--contact);
  }
  .contact-list li {
    display: flex;
    align-items: flex-start;
    line-height: 24px;
  }
  .contact-list .icon {
    flex: none;
    width: 13px;
    height: 13px;
    margin: 5px 7px 0 0;
  }
  .contact-list .address span { display: block; }
  .caption {
    position: absolute;
    left: 0;
    width: 1155px;
    text-align: center;
    font-family: "Montserrat", sans-serif;
    font-weight: 500;
    font-size: 26px;
    letter-spacing: 4px;
    color: var(--caption);
    font-variant: small-caps;
  }
  .caption-front { top: 578px; }
  .caption-back { top: 1116px; }
</style>
</head>
<body>
<div class="canvas">

  <section class="card card-front" aria-label="Business card front">
    <div class="brand">
      <span class="brand-mark"></span>
      Corbel Ridge Manor Banquet<br>&amp; Convention Centre
    </div>

    <div class="contact-panel">
      <p class="person-name">Marco Bellandi</p>
      <p class="person-role">Owner / C.E.O</p>
      <ul class="contact-list">
        <li class="address">
          <svg class="icon" viewBox="0 0 12 12"><circle cx="6" cy="6" r="6" fill="var(--gold)"/><path d="M6 2.6a2.2 2.2 0 0 0-2.2 2.2C3.8 6.6 6 9.4 6 9.4s2.2-2.8 2.2-4.6A2.2 2.2 0 0 0 6 2.6z" fill="var(--charcoal)"/></svg>
          <div><span>Suite # 118, Vale Hall,</span><span>NY 40912</span></div>
        </li>
        <li>
          <svg class="icon" viewBox="0 0 12 12"><circle cx="6" cy="6" r="6" fill="var(--gold)"/><path d="M4 3l1.2 1.6-.6.8a4 4 0 0 0 2 2l.8-.6L9 8l-.8 1C6 9 3 6 3 3.8z" fill="var(--charcoal)"/></svg>
          555-204-1187
        </li>
        <li>
          <svg class="icon" viewBox="0 0 12 12"><circle cx="6" cy="6" r="6" fill="var(--gold)"/><rect x="4" y="2.6" width="4" height="6.8" rx="0.8" fill="var(--charcoal)"/></svg>
          555-318-6620
        </li>
        <li>
          <svg class="icon" viewBox="0 0 12 12"><circle cx="6" cy="6" r="6" fill="var(--gold)"/><rect x="3" y="4.4" width="6" height="4" fill="var(--charcoal)"/><rect x="4" y="2.8" width="4" height="1.6" fill="var(--charcoal)"/></svg>
          555-472-9035
        </li>
        <li>
          <svg class="icon" viewBox="0 0 12 12"><circle cx="6" cy="6" r="6" fill="var(--gold)"/><rect x="3" y="3.8" width="6" height="4.4" fill="var(--charcoal)"/><path d="M3 3.8 6 6.4 9 3.8" stroke="var(--gold)" stroke-width="0.7" fill="none"/></svg>
          events@corbelridgemanor.com
        </li>
        <li>
          <svg class="icon" viewBox="0 0 12 12"><circle cx="6" cy="6" r="6" fill="var(--gold)"/><circle cx="6" cy="6" r="3" fill="none" stroke="var(--charcoal)" stroke-width="0.9"/><path d="M3 6h6M6 3v6" stroke="var(--charcoal)" stroke-width="0.7"/></svg>
          www.corbelridgemanor.com
        </li>
      </ul>
    </div>
  </section>

  <div class="caption caption-front">Business Card Front</div>

  <section class="card card-back" aria-label="Business card back">
    <div class="brand">
      <span class="brand-mark"></span>
      Corbel Ridge Manor Banquet<br>&amp; Convention Centre
    </div>
  </section>

  <div class="caption caption-back">Business Card Back</div>

</div>
</body>
</html>
```